Kestrel Gardenworks Business Card

An eye catching, yet simple business card that includes;

1. our logo
2. office phone - 5083172946
3. email - kestrelgardenworks@mailbrook.com
4. website - www.kestrelgardenworks.com
5. instagram - @kestrelgardenworksnv

```html
<!DOCTYPE html>
<html lang="en">
<head>
<meta charset="utf-8">
<title>Kestrel Gardenworks Business Card</title>
<link href="https://fonts.googleapis.com/css2?family=Roboto:wght@400;500;700;900&display=swap" rel="stylesheet">
<style>
  :root {
    --bg: #232323;
    --card-dark: #1f2021;
    --card-light: #f1f1f1;
    --brown: #8a4f22;
    --ink: #1c1c1c;
    --muted-ink: #4a4c4e;
    --footer-text: #d4d4d4;
    --band-dark: #3a3b3c;
  }
  * { margin: 0; padding: 0; box-sizing: border-box; }
  html, body {
    width: 1200px; height: 576px; overflow: hidden;
    background: var(--bg);
    font-family: "Roboto", Arial, sans-serif;
  }
  .canvas { position: relative; width: 1200px; height: 576px; }

  .card { position: absolute; border-radius: 10px; overflow: hidden; }

  /* Front: dark card */
  .card-front {
    left: 102px; top: 138px; width: 484px; height: 294px;
    background: var(--card-dark);
  }
  .front-brand {
    position: absolute; left: 0; top: 70px; width: 100%;
    display: flex; align-items: center; justify-content: center; gap: 14px;
  }
  .front-brand .brand-dot {
    width: 30px; height: 30px; border-radius: 50%; background: var(--muted-ink);
  }
  .front-brand .brand-name {
    font-weight: 900; font-size: 40px; line-height: 1.05;
    color: var(--muted-ink); text-transform: uppercase; letter-spacing: 1px;
  }
  .front-footer {
    position: absolute; left: 0; bottom: 30px; width: 100%;
    display: flex; justify-content: center; align-items: center; gap: 8px;
    font-size: 11.5px; color: var(--footer-text);
  }
  .front-footer .item { display: flex; align-items: center; gap: 5px; }

  /* Back: light card */
  .card-back {
    left: 596px; top: 138px; width: 480px; height: 292px;
    background: var(--card-light);
  }
  .back-brand {
    position: absolute; left: 22px; top: 116px;
    display: flex; align-items: center; gap: 8px;
  }
  .back-brand .brand-dot {
    width: 20px; height: 20px; border-radius: 50%; background: var(--brown);
  }
  .back-brand .brand-name {
    font-weight: 900; font-size: 18px; line-height: 1.1;
    color: var(--ink); text-transform: uppercase;
  }
  .contact { position: absolute; left: 234px; top: 71px; width: 236px; }
  .contact .person-name { font-weight: 700; font-size: 18px; color: var(--brown); white-space: nowrap; }
  .contact .person-role { font-size: 12.5px; color: var(--ink); margin-top: 3px; }
  .contact-list { list-style: none; margin-top: 14px; }
  .contact-list li {
    display: flex; align-items: center; gap: 9px;
    font-size: 12px; color: var(--ink); height: 18.5px; white-space: nowrap;
  }
  .contact-list svg { width: 11px; height: 11px; flex: none; }

  .back-band { position: absolute; left: 0; bottom: 0; width: 480px; height: 36px; }
  .band-social {
    position: absolute; left: 258px; bottom: 10px;
    display: flex; align-items: center; gap: 6px;
    font-size: 11.5px; color: #f0e6dc;
  }
  .social-dot { width: 11px; height: 11px; border-radius: 3px; background: currentColor; opacity: .8; }
</style>
</head>
<body>
<div class="canvas">

  <section class="card card-front">
    <div class="front-brand">
      <span class="brand-dot"></span>
      <span class="brand-name">Kestrel<br>Gardenworks</span>
    </div>
    <div class="front-footer">
      <span class="item"><span class="social-dot"></span>@kestrelgardenworksnv</span>
      <span class="item">
        <svg width="12" height="12" viewBox="0 0 12 12" fill="none" stroke="#3a8fd0" stroke-width="1.1">
          <circle cx="6" cy="6" r="5"/><ellipse cx="6" cy="6" rx="2.2" ry="5"/><path d="M1 6h10M2 3.3h8M2 8.7h8"/>
        </svg>
        www.kestrelgardenworks.com
      </span>
    </div>
  </section>

  <section class="card card-back">
    <div class="back-brand">
      <span class="brand-dot"></span>
      <span class="brand-name">Kestrel<br>Gardenworks</span>
    </div>

    <div class="contact">
      <div class="person-name">Marcus Hale Bennett</div>
      <div class="person-role">Managing Director</div>
      <ul class="contact-list">
        <li>
          <svg viewBox="0 0 12 12" fill="var(--brown)"><path d="M1 4c0-1.5 2.5-2.5 5-2.5S11 2.5 11 4v1H8.5V3.8h-5V5H1zM2.5 6h7l1 5h-9z"/></svg>
          5083172946
        </li>
        <li>
          <svg viewBox="0 0 12 12" fill="none" stroke="var(--brown)" stroke-width="1.4"><rect x="1" y="2.5" width="10" height="7"/><path d="M1 2.5l5 4 5-4"/></svg>
          kestrelgardenworks@mailbrook.com
        </li>
        <li>
          <svg viewBox="0 0 12 12" fill="none" stroke="var(--brown)" stroke-width="1.1"><circle cx="6" cy="6" r="5"/><ellipse cx="6" cy="6" rx="2.2" ry="5"/><path d="M1 6h10"/></svg>
          www.kestrelgardenworks.com
        </li>
      </ul>
    </div>

    <svg class="back-band" viewBox="0 0 480 36" preserveAspectRatio="none">
      <rect x="0" y="24" width="480" height="12" fill="var(--band-dark)"/>
      <path d="M218 36 L232 8 Q234 4 240 4 H480 V36 Z" fill="var(--brown)"/>
    </svg>
    <div class="band-social"><span class="social-dot"></span>@kestrelgardenworksnv</div>
  </section>

</div>
</body>
</html>
```